Groundbreaking Orthopaedic Clinic Postcard

We are looking to announce the groundbreaking of a new building, so there is your headline. Take a look at the attached Word file for the building specifics. You can use your imagination for the bullet points. This will be two-sided with the one of the pictures spread over the two pages as you creatively see possible. You can try a starred map with the rough location of Hattiesburg on the back. We will need room for the standard postal address and stamp on one side as well. Use the attached postcard as a reference, but this one can look much different. Looking for different ideas. I would want our logo and our mailing information just like the other postcard. Use the contact information for Corwin Aldebrook, Senior Vice President, 555-317-8290, caldebrook@veltrongroup.example, www.VeltronGroup.example. Somewhere on the back, we will want to advertise our services to others. Perhaps some form of the last few sentences in the Word document. I will make constant comments, so feel free to submit multiple designs. I will make a winner before 10 days, so move quickly. Good luck!

Target Market(s)

Physician groups and hospital CEOs.

Font styles to use
Serif
Sans Serif

Colors
33b8a4
33a6d7
85acd3
0555a3
3176b5
0292cd
876aae
b7a5cd
ec1f27

Requirements
Must have
• All of the contact information for our company clearly.
Nice to have
• Something a bit more eye-catching and different than the same postcards we always get.
Should not have
• No crazy cursive writing or bright yellows or pinks. It should be exciting but not flashy.

```html
<!DOCTYPE html>
<html lang="en">
<head>
<meta charset="utf-8">
<title>Veltron Group – Groundbreaking Postcard</title>
<link rel="stylesheet" href="https://fonts.googleapis.com/css2?family=Playfair+Display:wght@400;700&family=Mulish:wght@400;600;700;800&display=swap">
<style>
  :root {
    --navy: #0555a3;
    --blue: #3176b5;
    --bright: #0292cd;
    --sky: #33a6d7;
    --pale: #85acd3;
    --teal: #33b8a4;
    --purple: #876aae;
    --lilac: #b7a5cd;
    --ink: #4a4a4a;
    --grey: #6b6b6b;
    --rule: #bdbdbd;
    --paper: #ffffff;
    --stage: #e9eaec;
    --serif: "Playfair Display", Georgia, serif;
    --sans: "Mulish", Arial, sans-serif;
  }
  * { box-sizing: border-box; margin: 0; padding: 0; }
  html, body { width: 1051px; height: 1200px; overflow: hidden; }
  body { background: var(--stage); font-family: var(--sans); position: relative; }

  .postcard {
    position: absolute; left: 85px; width: 880px; height: 570px;
    background: var(--paper); overflow: hidden;
    box-shadow: 0 4px 14px rgba(0,0,0,.18);
  }
  .postcard--front { top: 20px; }
  .postcard--back { top: 610px; }
  .postcard > svg.shapes { position: absolute; inset: 0; }
  .abs { position: absolute; }

  .brand-name { font-family: var(--serif); font-weight: 400; color: var(--navy); line-height: .95; }

  /* front – left panel */
  .front-brand { left: 12px; top: 16px; font-size: 50px; }
  .front-brand span { display: block; font-size: 38px; margin-top: 8px; }
  .kicker { font-family: var(--serif); font-size: 10.5px; letter-spacing: 6px; color: var(--grey); text-transform: uppercase; }
  .front-kicker { left: 14px; top: 140px; }
  .tag {
    display: inline-block; background: var(--teal); color: #fff;
    font-size: 11.5px; font-weight: 600; padding: 3px 8px 3px 12px; text-transform: uppercase;
    box-shadow: 2px 2px 0 rgba(0,0,0,.15);
  }
  .front-tags { left: 0; top: 165px; }
  .front-tags .tag { display: block; width: fit-content; margin-bottom: 9px; }
  .front-tags .tag:first-child { padding-right: 30px; }
  .front-region { left: 14px; top: 234px; letter-spacing: 3px; font-weight: 700; font-size: 10px; color: var(--ink); }
  .facility { left: 14px; top: 262px; width: 265px; font-size: 8.6px; color: var(--ink); line-height: 1.4; }
  .facility p { margin-bottom: 8px; }
  .feature-list { list-style: none; }
  .feature-list li { display: flex; align-items: center; gap: 9px; margin-bottom: 9px; }
  .dot { width: 15px; height: 15px; border-radius: 50%; background: var(--lilac); flex: none; position: relative; }
  .dot::after { content: ""; position: absolute; inset: 4px; border-radius: 50%; background: var(--purple); }
  .sports { display: grid; grid-template-columns: 1fr 1fr; column-gap: 10px; }
  .site-tag { font-size: 11px; text-transform: none; display: flex; align-items: center; gap: 6px; padding: 4px 14px 4px 12px; }
  .site-tag::before { content: ""; width: 9px; height: 9px; border: 1.5px solid #fff; border-radius: 50%; }
  .front-site { left: 0; bottom: 14px; }

  /* front – centre band */
  .contact-head { left: 295px; top: 28px; width: 400px; text-align: center; color: #fff; }
  .contact-head h2 { font-size: 28px; font-weight: 800; letter-spacing: .5px; }
  .contact-head p { font-size: 18px; margin-top: 2px; }
  .seal-name { left: 288px; top: 238px; width: 300px; text-align: center; font-size: 50px; }
  .seal-name span { display: block; font-size: 34px; margin-top: 6px; }
  .call { left: 295px; top: 485px; width: 290px; text-align: center; color: #fff; }
  .call p { font-size: 28px; font-weight: 400; line-height: 1; }
  .call strong { display: block; font-size: 28px; font-weight: 800; margin-top: 2px; }

  /* back */
  .back-brand { left: 18px; top: 22px; font-size: 72px; color: #fff; }
  .back-brand span { display: block; font-size: 46px; margin-top: 10px; }
  .back-about { left: 0; top: 220px; width: 410px; }
  .back-about .tag { font-size: 11.5px; }
  .back-about p { color: #fff; font-size: 10.6px; line-height: 1.5; padding: 14px 0 0 18px; text-align: justify; }
  .rep { left: 18px; top: 380px; color: #fff; }
  .rep h3 { font-size: 21px; font-weight: 800; }
  .rep small { font-size: 10.5px; font-weight: 700; }
  .rep-lines { left: 18px; top: 440px; color: #fff; font-size: 13.5px; font-weight: 700; list-style: none; }
  .rep-lines li { display: flex; align-items: center; gap: 12px; margin-bottom: 18px; }
  .icon { width: 22px; height: 22px; border-radius: 50%; background: #fff; display: grid; place-items: center; flex: none; }
  .back-site { left: 0; bottom: 16px; }
  .stamp {
    left: 733px; top: 25px; width: 127px; height: 126px; border: 1px solid var(--rule);
    display: grid; place-items: center; font-size: 13px; color: #333; text-transform: uppercase;
  }
  .address-lines { left: 496px; top: 249px; width: 364px; }
  .address-lines i { display: block; height: 1px; background: var(--rule); margin-bottom: 33px; }
  .barcode-box {
    left: 496px; top: 478px; width: 366px; height: 62px; border: 1px solid var(--rule);
    display: grid; place-items: center; font-size: 13px; color: #333; text-transform: uppercase;
  }
</style>
</head>
<body>

<!-- FRONT -->
<section class="postcard postcard--front">
  <svg class="shapes" viewBox="0 0 880 570" width="880" height="570">
    <defs>
      <linearGradient id="bandGrad" x1="0" y1="0" x2="0" y2="1">
        <stop offset="0" stop-color="#1f6cc0"/>
        <stop offset="1" stop-color="#0555a3"/>
      </linearGradient>
      <linearGradient id="photoGrad" x1="0" y1="0" x2="0" y2="1">
        <stop offset="0" stop-color="#2f7fcf"/>
        <stop offset=".55" stop-color="#c9d6e3"/>
        <stop offset=".85" stop-color="#9fb0bf"/>
        <stop offset="1" stop-color="#4f8a36"/>
      </linearGradient>
    </defs>
    <rect width="880" height="570" fill="#f4f5f6"/>
    <rect role="img" aria-label="Photograph of the new medical building against a blue sky with hedges in front" x="560" y="0" width="320" height="570" fill="url(#photoGrad)"/>
    <path d="M276 0 Q230 285 312 570 L330 570 Q248 285 296 0Z" fill="var(--teal)"/>
    <path d="M296 0 Q250 285 330 570 L345 570 Q266 285 314 0Z" fill="var(--sky)"/>
    <path d="M314 0 L700 0 Q720 285 650 570 L345 570 Q266 285 314 0Z" fill="url(#bandGrad)"/>
    <path d="M700 0 L716 0 Q736 285 666 570 L650 570 Q720 285 700 0Z" fill="var(--sky)"/>
    <path d="M716 0 L728 0 Q748 285 678 570 L666 570 Q736 285 716 0Z" fill="var(--teal)"/>
    <circle cx="438" cy="281" r="160" fill="#fff" stroke="var(--navy)" stroke-width="11"/>
  </svg>

  <h1 class="abs brand-name front-brand">VELTRON<span>GROUP</span></h1>
  <p class="abs kicker front-kicker">Breaks ground on</p>
  <div class="abs front-tags">
    <span class="tag">55,000 SF Orthopedic and</span>
    <span class="tag">Sports Performance Facility</span>
  </div>
  <p class="abs kicker front-region">In Southern Mississippi.</p>

  <div class="abs facility">
    <p>The new facility will also include -</p>
    <p>A connected 13,000 SF indoor sports performance center</p>
    <ul class="feature-list">
      <li><span class="dot"></span>Weight systems.</li>
      <li><span class="dot"></span>Half-court basketball floor.</li>
      <li><span class="dot"></span>Baseball batting net.</li>
      <li><span class="dot"></span>A partial turf football field.</li>
    </ul>
    <p>Which opens up to an exterior natural turf field, to accommodate</p>
    <ul class="feature-list sports">
      <li><span class="dot"></span>Football.</li>
      <li><span class="dot"></span>Volleyball.</li>
      <li><span class="dot"></span>Soccer.</li>
      <li><span class="dot"></span>Other sports training.</li>
    </ul>
  </div>
  <span class="abs tag site-tag front-site">www.VeltronGroup.example</span>

  <div class="abs contact-head">
    <h2>CORWIN ALDEBROOK</h2>
    <p>Senior Vice President</p>
  </div>
  <p class="abs brand-name seal-name">VELTRON<span>GROUP</span></p>
  <div class="abs call">
    <p>CALL US NOW</p>
    <strong>555-317-8290</strong>
  </div>
</section>

<!-- BACK -->
<section class="postcard postcard--back">
  <svg class="shapes" viewBox="0 0 880 570" width="880" height="570">
    <defs>
      <linearGradient id="backGrad" x1="0" y1="0" x2="1" y2="1">
        <stop offset="0" stop-color="#1f6cc0"/>
        <stop offset="1" stop-color="#0555a3"/>
      </linearGradient>
    </defs>
    <path d="M0 0 L420 0 Q500 285 408 570 L0 570Z" fill="var(--teal)"/>
    <path d="M0 0 L406 0 Q486 285 394 570 L0 570Z" fill="var(--sky)"/>
    <path d="M0 0 L392 0 Q470 285 380 570 L0 570Z" fill="url(#backGrad)"/>
  </svg>

  <h2 class="abs brand-name back-brand">VELTRON<span>GROUP</span></h2>
  <div class="abs back-about">
    <span class="tag">About Veltron Group</span>
    <p>Veltron Group is a nationally recognized developer of medical real estate. A full-service real estate company, Veltron Group is headquartered in Harbor Bend, Fla. Veltron Group’s team has developed more than 7 million square feet and acquired 1.7 million square feet of medical and related real estate in the past 30 years. Veltron Group’s objective is to support healthcare providers to more effectively address the issues associated with developing real estate assets in today’s changing healthcare market.</p>
  </div>
  <div class="abs rep">
    <h3>CORWIN ALDEBROOK</h3>
    <small>Senior Vice President</small>
  </div>
  <ul class="abs rep-lines">
    <li><span class="icon"><svg width="12" height="12" viewBox="0 0 24 24"><path d="M6.6 10.8a15 15 0 0 0 6.6 6.6l2.2-2.2a1 1 0 0 1 1-.25 11.4 11.4 0 0 0 3.6.57 1 1 0 0 1 1 1V20a1 1 0 0 1-1 1A17 17 0 0 1 3 4a1 1 0 0 1 1-1h3.5a1 1 0 0 1 1 1c0 1.250.2 2.45.57 3.57a1 1 0 0 1-.25 1z" fill="#0555a3"/></svg></span>555-317-8290</li>
    <li><span class="icon"><svg width="12" height="10" viewBox="0 0 24 18"><rect x="1" y="1" width="22" height="16" rx="2" fill="none" stroke="#0555a3" stroke-width="2.5"/><path d="M2 2l10 8 10-8" fill="none" stroke="#0555a3" stroke-width="2.5"/></svg></span>caldebrook@veltrongroup.example</li>
  </ul>
  <span class="abs tag site-tag back-site">www.VeltronGroup.example</span>

  <div class="abs stamp">Stamp</div>
  <div class="abs address-lines"><i></i><i></i><i></i><i></i></div>
  <div class="abs barcode-box">Barcode</div>
</section>

</body>
</html>
```